Trade Show Booth Wall Graphics Design (Beauty Industry)

We are a beauty/nail supply distributor that supplies products used in professional nail salons. Our target customers are Nail Salons. We are looking for a wall panel graphic design that will be placed on the walls of our trade show booth (see attached image for reference).
These wall panels will act as an aesthetic background and highlight the key product offerings to customers as they view our booth. The primary goal of each wall panel design should focus on the product name and image. Backgrounds for each wall panel may include professional/stock photography to give context or visualization, color pattern or wave design to create a sense of “flow” between products, and/or any general use of colors to provide a professional, simple, and clear product message to viewers.
Each wall panel, and designated products, is based on product category and similarity of function/use.
Nail Salons
Beauty

```html
<!DOCTYPE html>
<html lang="en">
<head>
<meta charset="utf-8">
<title>Booth Wall Panels – Options 03 &amp; 04</title>
<link href="https://fonts.googleapis.com/css2?family=Nunito:wght@700;800;900&family=Open+Sans:wght@700&display=swap" rel="stylesheet">
<style>
  :root{
    --board-dark:#58585a;
    --board-light:#6c6c6f;
    --title-grey:#a8a8aa;
    --brick:#b9b9bb;
    --brick-dark:#a9a9ab;
    --ink:#2b2b2d;
    --white:#ffffff;
    --header-grey:#b5b5b7;
    --swoosh:#2c2c2e;
    --olive:#8b7c17;
    --navy:#1f3b8c;
    --violet:#7b2c99;
  }
  *{box-sizing:border-box;margin:0;padding:0}
  html,body{width:1200px;height:850px;overflow:hidden}
  body{position:relative;background:var(--board-dark);font-family:"Nunito",sans-serif}
  .board-bg{position:absolute;inset:0}
  .option-title{position:absolute;left:761px;font-family:"Open Sans",sans-serif;font-weight:700;font-size:41px;color:var(--title-grey);letter-spacing:.5px}
  .option-title.o3{top:38px}
  .option-title.o4{top:416px}

  .wall{position:absolute;left:111px;width:978px;height:287px;display:flex;box-shadow:0 3px 8px rgba(0,0,0,.35);overflow:hidden}
  .wall.o3{top:112px;
    background-color:var(--brick);
    background-image:
      linear-gradient(var(--brick-dark) 1px,transparent 1px),
      linear-gradient(90deg,var(--brick-dark) 1px,transparent 1px);
    background-size:52px 17px,52px 34px;}
  .wall.o4{top:482px;background:linear-gradient(135deg,#f4f4f5,#e2e2e4 40%,#f6f6f7 60%,#dcdcde)}

  .col{position:relative;height:100%;display:flex;flex-direction:column}
  .col.narrow{width:122px}
  .col.wide{width:245px}
  .o3 .col.narrow{border-right:1px solid rgba(255,255,255,.35)}
  .o3 .col.wide{border-right:1px solid rgba(255,255,255,.35)}

  .col-head{height:50px;display:flex;align-items:center;justify-content:center;text-align:center;font-weight:800;font-size:11px;line-height:1.22;color:var(--white)}
  .o3 .col-head{border-bottom:1.5px solid var(--white);text-shadow:0 1px 1px rgba(0,0,0,.25)}
  .o3 .col.wide .col-head{border-bottom:1.5px solid var(--white)}
  .o4 .col.narrow{background:var(--white)}
  .o4 .col-head{height:46px;background:var(--header-grey);color:var(--ink)}
  .swoosh{display:block;width:122px;height:30px;margin-top:-1px}

  .items{flex:1;display:flex;flex-direction:column;justify-content:space-around;padding:10px 8px 12px}
  .o4 .items{padding-top:0}
  .item{display:flex;align-items:center;justify-content:space-between;gap:4px}
  .label{font-weight:800;font-size:9.2px;line-height:1.12;color:var(--white)}
  .o4 .label{color:var(--ink)}
  .label small{display:block;font-size:4.8px;font-weight:700;line-height:1.1}
  .o4 .label.olive{color:var(--olive)}
  .o4 .label.navy{color:var(--navy)}
  .o4 .label.violet{color:var(--violet)}

  .shot{flex:none;border-radius:3px}
  .s-paraffin{width:46px;height:48px;background:linear-gradient(90deg,#4a3a8f 0 48%,transparent 48% 52%,#e36b2c 52%)}
  .s-tins{width:60px;height:46px;border-radius:10px;background:radial-gradient(circle at 30% 70%,#f2d26c 0 20%,transparent 21%),radial-gradient(circle at 70% 70%,#ef8fa0 0 20%,transparent 21%),radial-gradient(circle at 50% 25%,#9fcfb7 0 20%,transparent 21%)}
  .s-bag{width:52px;height:30px;background:linear-gradient(160deg,#f3e6d0,#dcc8a6)}
  .s-roll{width:52px;height:32px;border-radius:16px 4px 4px 16px;background:linear-gradient(90deg,#e8eef2,#ffffff)}
  .s-gel{width:40px;height:44px;background:linear-gradient(90deg,#3d2418 0 55%,transparent 55% 62%,#ececec 62%)}
  .s-kit{width:52px;height:30px;background:linear-gradient(90deg,#f4f4f6 0 55%,#7a57b8 55%)}
  .s-liner{width:60px;height:30px;border-radius:14px;background:linear-gradient(90deg,#d7dde2,#4a8fe0)}
  .s-pouch{width:52px;height:34px;background:linear-gradient(180deg,#8cc4e6,#e9f3f8 60%,#5fb28e)}
  .s-buf-ow{width:44px;height:34px;background:linear-gradient(135deg,#f2774a,#f7a078)}
  .s-buf-ob{width:44px;height:34px;background:linear-gradient(135deg,#f07a3a 0 45%,#222 45%)}
  .s-buf-pb{width:44px;height:34px;background:linear-gradient(135deg,#7b58c2 0 45%,#1e1e20 45%)}
  .s-zebra{width:44px;height:36px;background:linear-gradient(160deg,#e4e6e8,#9ea3a8)}
</style>
</head>
<body>
  <svg class="board-bg" width="1200" height="850" aria-hidden="true">
    <polygon points="1200,0 1200,850 0,850" fill="var(--board-light)"/>
    <polygon points="0,778 105,850 0,850" fill="var(--board-dark)"/>
  </svg>

  <div class="option-title o3">Option-03</div>
  <section class="wall o3">
    <div class="col narrow">
      <h2 class="col-head">CALM &amp; GENTLE<br>WAXING</h2>
      <div class="items">
        <div class="item"><span class="label">PARAFFIN<br>WAX</span><div class="shot s-paraffin" role="img" aria-label="Paraffin wax packs"></div></div>
        <div class="item"><div class="shot s-tins" role="img" aria-label="Wax tins"></div><span class="label">LUMI WAX</span></div>
        <div class="item"><span class="label">PARAFFIN<br>BAG</span><div class="shot s-bag" role="img" aria-label="Paraffin bag roll"></div></div>
        <div class="item"><div class="shot s-roll" role="img" aria-label="Wax fabric roll"></div><span class="label">WAX<br>FABRIC<br>ROLL</span></div>
      </div>
    </div>
    <div class="col wide"></div>
    <div class="col narrow">
      <h2 class="col-head">Brilliant Shine<br>&amp; Rich Colors</h2>
      <div class="items">
        <div class="item"><span class="label">Lumi Gel<br>Topcoat</span><div class="shot s-gel" role="img" aria-label="Gel topcoat bottles"></div></div>
        <div class="item"><div class="shot s-gel" role="img" aria-label="Gel basecoat bottles"></div><span class="label">Lumi Gel<br>Basecoat</span></div>
        <div class="item"><span class="label">Lumi Gel<br>Black</span><div class="shot s-gel" role="img" aria-label="Black gel polish bottles"></div></div>
        <div class="item"><div class="shot s-gel" role="img" aria-label="White gel polish bottles"></div><span class="label">Lumi Gel<br>White</span></div>
      </div>
    </div>
    <div class="col wide"></div>
    <div class="col narrow">
      <h2 class="col-head">Individual<br>Perfection</h2>
      <div class="items">
        <div class="item"><span class="label">Disposable<br>Pedicure<br>Kit</span><div class="shot s-kit" role="img" aria-label="Disposable pedicure kit"></div></div>
        <div class="item"><div class="shot s-kit" role="img" aria-label="Disposable manicure kit"></div><span class="label">Disposable<br>Manicure<br>Kit</span></div>
        <div class="item"><span class="label">Pedicure<br>Liner</span><div class="shot s-liner" role="img" aria-label="Pedicure liners"></div></div>
        <div class="item"><div class="shot s-pouch" role="img" aria-label="Sterilization pouches"></div><span class="label">Sterilization<br>Pouch</span></div>
      </div>
    </div>
    <div class="col narrow">
      <h2 class="col-head">The Foundation<br>of Every Manicure</h2>
      <div class="items">
        <div class="item"><span class="label">3-Way<br>Buffer<small>(Orange/White)</small></span><div class="shot s-buf-ow" role="img" aria-label="Orange and white buffer"></div></div>
        <div class="item"><div class="shot s-buf-ob" role="img" aria-label="Orange and black buffer"></div><span class="label">3-Way<br>Buffer<small>(Orange/Black)</small></span></div>
        <div class="item"><span class="label">3-Way<br>Buffer<small>(Purple/Black)</small></span><div class="shot s-buf-pb" role="img" aria-label="Purple and black buffer"></div></div>
        <div class="item"><div class="shot s-zebra" role="img" aria-label="Regular zebra files"></div><span class="label">Premium<br>Zebra File<small>(Regular)</small></span></div>
        <div class="item"><span class="label">VPremium<br>Zebra File<small>(Jumbo)</small></span><div class="shot s-zebra" role="img" aria-label="Jumbo zebra files"></div></div>
      </div>
    </div>
  </section>

  <div class="option-title o4">Option-04</div>
  <section class="wall o4" role="img" aria-label="White faceted geometric wall background">
    <div class="col narrow">
      <h2 class="col-head">CALM &amp; GENTLE<br>WAXING</h2>
      <svg class="swoosh" viewBox="0 0 122 30" aria-hidden="true"><rect width="122" height="30" fill="var(--header-grey)"/><path d="M0 14 Q55 -6 122 8 V30 H0Z" fill="var(--swoosh)"/><path d="M0 30 Q55 6 122 22 V30Z" fill="var(--white)"/></svg>
      <div class="items">
        <div class="item"><span class="label">PARAFFIN<br>WAX</span><div class="shot s-paraffin" role="img" aria-label="Paraffin wax packs"></div></div>
        <div class="item"><div class="shot s-tins" role="img" aria-label="Wax tins"></div><span class="label">LUMI WAX</span></div>
        <div class="item"><span class="label">PARAFFIN<br>BAG</span><div class="shot s-bag" role="img" aria-label="Paraffin bag roll"></div></div>
        <div class="item"><div class="shot s-roll" role="img" aria-label="Wax fabric roll"></div><span class="label">WAX<br>FABRIC<br>ROLL</span></div>
      </div>
    </div>
    <div class="col wide"></div>
    <div class="col narrow">
      <h2 class="col-head">Brilliant Shine<br>&amp; Rich Colors</h2>
      <svg class="swoosh" viewBox="0 0 122 30" aria-hidden="true"><rect width="122" height="30" fill="var(--header-grey)"/><path d="M0 14 Q55 -6 122 8 V30 H0Z" fill="var(--swoosh)"/><path d="M0 30 Q55 6 122 22 V30Z" fill="var(--white)"/></svg>
      <div class="items">
        <div class="item"><span class="label">Lumi Gel<br>Topcoat</span><div class="shot s-gel" role="img" aria-label="Gel topcoat bottles"></div></div>
        <div class="item"><div class="shot s-gel" role="img" aria-label="Gel basecoat bottles"></div><span class="label olive">Lumi Gel<br>Basecoat</span></div>
        <div class="item"><span class="label navy">Lumi Gel<br>Black</span><div class="shot s-gel" role="img" aria-label="Black gel polish bottles"></div></div>
        <div class="item"><div class="shot s-gel" role="img" aria-label="White gel polish bottles"></div><span class="label violet">Lumi Gel<br>White</span></div>
      </div>
    </div>
    <div class="col wide"></div>
    <div class="col narrow">
      <h2 class="col-head">Individual<br>Perfection</h2>
      <svg class="swoosh" viewBox="0 0 122 30" aria-hidden="true"><rect width="122" height="30" fill="var(--header-grey)"/><path d="M0 14 Q55 -6 122 8 V30 H0Z" fill="var(--swoosh)"/><path d="M0 30 Q55 6 122 22 V30Z" fill="var(--white)"/></svg>
      <div class="items">
        <div class="item"><span class="label">Disposable<br>Pedicure<br>Kit</span><div class="shot s-kit" role="img" aria-label="Disposable pedicure kit"></div></div>
        <div class="item"><div class="shot s-kit" role="img" aria-label="Disposable manicure kit"></div><span class="label">Disposable<br>Manicure<br>Kit</span></div>
        <div class="item"><span class="label">Pedicure<br>Liner</span><div class="shot s-liner" role="img" aria-label="Pedicure liners"></div></div>
        <div class="item"><div class="shot s-pouch" role="img" aria-label="Sterilization pouches"></div><span class="label">Sterilization<br>Pouch</span></div>
      </div>
    </div>
    <div class="col narrow">
      <h2 class="col-head">The Foundation<br>of Every Manicure</h2>
      <svg class="swoosh" viewBox="0 0 122 30" aria-hidden="true"><rect width="122" height="30" fill="var(--header-grey)"/><path d="M0 14 Q55 -6 122 8 V30 H0Z" fill="var(--swoosh)"/><path d="M0 30 Q55 6 122 22 V30Z" fill="var(--white)"/></svg>
      <div class="items">
        <div class="item"><span class="label">3-Way<br>Buffer<small>(Orange/White)</small></span><div class="shot s-buf-ow" role="img" aria-label="Orange and white buffer"></div></div>
        <div class="item"><div class="shot s-buf-ob" role="img" aria-label="Orange and black buffer"></div><span class="label">3-Way<br>Buffer<small>(Orange/Black)</small></span></div>
        <div class="item"><span class="label">3-Way<br>Buffer<small>(Purple/Black)</small></span><div class="shot s-buf-pb" role="img" aria-label="Purple and black buffer"></div></div>
        <div class="item"><div class="shot s-zebra" role="img" aria-label="Regular zebra files"></div><span class="label">Premium<br>Zebra File<small>(Regular)</small></span></div>
        <div class="item"><span class="label">VPremium<br>Zebra File<small>(Jumbo)</small></span><div class="shot s-zebra" role="img" aria-label="Jumbo zebra files"></div></div>
      </div>
    </div>
  </section>
</body>
</html>
```